Flyer Design Project

I need a cool design that describes a new line of services I am selling. The final product should be a 8 1/2 by 11 and maximum two pages.

I am selling consulting services to learn to use web conferencing tools for business development, meeting and training.

Please use the file I have attached as a guide for your work. It is a document called "primer-thriftyhacksguide" and I love its design.

Thanks

                                        Please substitute the new text availble and just uploaded in the FLYER. Please submit the FINAL version fo your design with TExt changes as well as improvements detailed in previous message. 

Target Market(s)

Entrepreneurs and classroom educators who wnats to explore a new way to teach (innovators not scared of technology)

Industry/Entity Type

Business

Requirements
Must have
• I would like to receive a final PDF with the content EDITABLE for minor edits (I have acrobat)
Logo should be included (attached)

PLEASE CHECK OUT ATTACHED DOCUMENT WHOSE DESIGN I LOVE.
IT is called "Primer thrifty-hacks guide". If you could follow that as a template to design mine that would be great!

```html
<!DOCTYPE html>
<html lang="en">
<head>
<meta charset="utf-8">
<title>Convenia Consulting – Online Engagement Services</title>
<link href="https://fonts.googleapis.com/css2?family=Arimo:wght@400;700&display=swap" rel="stylesheet">
<style>
  :root {
    --orange: #f58220;
    --ink: #1a1a1a;
    --white: #ffffff;
    --arrow: #7a3a12;
    --tab-1: #ffc20e;
    --tab-2: #f9a51a;
    --tab-3: #f58220;
    --tab-4: #f15a29;
    --tab-5: #ed1c24;
    --tab-6: #be1e2d;
    --tab-7: #8b1717;
    --bg-1: #fff7dc;
    --bg-2: #fff1d6;
    --bg-3: #feead3;
    --bg-4: #fde4d0;
    --bg-5: #fbdfcd;
    --bg-6: #f7d9cb;
    --bg-7: #f2d3c6;
  }
  * { box-sizing: border-box; margin: 0; padding: 0; }
  html, body { width: 849px; height: 1200px; overflow: hidden; background: var(--white); }
  .flyer {
    position: relative; width: 849px; height: 1200px; overflow: hidden;
    font-family: "Arimo", Arial, sans-serif; color: var(--ink); background: var(--white);
  }
  .backdrop { position: absolute; inset: 0; }
  .brand { position: absolute; left: 38px; top: 46px; display: flex; align-items: center; gap: 6px; }
  .brand-name { font-size: 19px; font-weight: 700; letter-spacing: 0.6px; color: var(--ink); }
  .brand-mark { width: 11px; height: 11px; border-radius: 50%; background: var(--orange); }
  .brand-tagline { position: absolute; left: 82px; top: 77px; font-size: 9px; color: var(--ink); }
  .headline {
    position: absolute; right: 66px; top: 78px; text-align: right; white-space: nowrap;
    font-size: 20px; font-weight: 700; line-height: 31px; color: var(--orange);
  }
  .services { position: absolute; left: 228px; top: 224px; width: 560px; list-style: none; }
  .service {
    position: relative; display: flex; align-items: center;
    border: 1px solid var(--orange); border-right: none; border-bottom: none;
    padding: 6px 21px 6px 39px;
  }
  .service:last-child { border-bottom: 1px solid var(--orange); }
  .service::before {
    content: ""; position: absolute; left: 0; top: 0; bottom: 0; width: 15px;
    background: var(--tab); border-radius: 8px 0 0 8px;
  }
  .service p { position: relative; font-size: 13.6px; line-height: 19.5px; text-align: justify; }
  .service-arrow { position: absolute; left: -15px; top: 5px; width: 12px; height: 10px; }
  .s1 { --tab: var(--tab-1); background: var(--bg-1); height: 131px; }
  .s2 { --tab: var(--tab-2); background: var(--bg-2); height: 111px; }
  .s3 { --tab: var(--tab-3); background: var(--bg-3); height: 92px; }
  .s4 { --tab: var(--tab-4); background: var(--bg-4); height: 93px; }
  .s5 { --tab: var(--tab-5); background: var(--bg-5); height: 93px; }
  .s6 { --tab: var(--tab-6); background: var(--bg-6); height: 71px; }
  .s7 { --tab: var(--tab-7); background: var(--bg-7); height: 71px; }
  .intro { position: absolute; left: 228px; top: 900px; width: 560px; font-size: 13.6px; line-height: 19.5px; text-align: justify; }
  .call { position: absolute; right: 62px; top: 1103px; color: var(--white); font-size: 17px; white-space: nowrap; }
  .call strong { font-weight: 700; }
  .call .phone { font-size: 27px; font-weight: 700; }
</style>
</head>
<body>
<div class="flyer">
  <svg class="backdrop" width="849" height="1200" viewBox="0 0 849 1200" aria-hidden="true">
    <defs>
      <linearGradient id="sidePanel" x1="0" y1="0" x2="1" y2="0">
        <stop offset="0" stop-color="#f47b20"/>
        <stop offset="0.55" stop-color="#f9b27a"/>
        <stop offset="1" stop-color="#ffffff"/>
      </linearGradient>
      <linearGradient id="sideFade" x1="0" y1="0" x2="0" y2="1">
        <stop offset="0" stop-color="#ffffff" stop-opacity="1"/>
        <stop offset="0.18" stop-color="#ffffff" stop-opacity="0.15"/>
        <stop offset="1" stop-color="#ffffff" stop-opacity="0"/>
      </linearGradient>
      <linearGradient id="swoosh" x1="0" y1="0" x2="0" y2="1">
        <stop offset="0" stop-color="#f7941d"/>
        <stop offset="0.5" stop-color="#e8661a"/>
        <stop offset="1" stop-color="#c04a12"/>
      </linearGradient>
      <linearGradient id="footerBand" x1="0" y1="0" x2="1" y2="0">
        <stop offset="0" stop-color="#f9b27a"/>
        <stop offset="0.4" stop-color="#f58220"/>
        <stop offset="1" stop-color="#f26b1d"/>
      </linearGradient>
    </defs>
    <rect x="0" y="0" width="240" height="1200" fill="url(#sidePanel)" role="img" aria-label="Soft orange panel with faint binary digits"/>
    <rect x="0" y="0" width="240" height="1200" fill="url(#sideFade)"/>
    <path d="M330 0 H470 C330 120 250 260 234 520 C224 760 222 960 224 1130 H208 C204 960 204 760 210 520 C220 280 258 120 330 0 Z" fill="url(#swoosh)"/>
    <path d="M0 1110 C250 1075 560 1072 849 1058 V1200 H0 Z" fill="#fde0c6"/>
    <path d="M0 1140 C260 1100 560 1088 849 1078 V1200 H0 Z" fill="url(#footerBand)"/>
  </svg>

  <div class="brand">
    <span class="brand-name">CONVENIA CONSULTING</span>
    <span class="brand-mark"></span>
  </div>
  <div class="brand-tagline">Coaching. Connection. Growth.</div>

  <h1 class="headline">Choose the service that best fit<br>your needs and budget. A new level<br>of online engagement and virtual<br>collaboration awaits.</h1>

  <ul class="services">
    <li class="service s1"><p><svg class="service-arrow" viewBox="0 0 12 10"><path d="M0 3.5H7V0L12 5L7 10V6.5H0Z" fill="var(--arrow)"/></svg>Webinar Series: Plan, design, develop and implement a 3+1 session webinar series about the content of your expertise marketed to live audiences with 3 hours of One-on-One online coaching on web conferencing tools and how to use them for your business. Includes access to online resource library of our Online Facilitator Certification plus access to your own online meeting room and virtual collaboration platform ($3,000).</p></li>
    <li class="service s2"><p><svg class="service-arrow" viewBox="0 0 12 10"><path d="M0 3.5H7V0L12 5L7 10V6.5H0Z" fill="var(--arrow)"/></svg>Webinar: Plan, design, develop and implement 1 webinar session on the content of your expertise marketed to live audiences with 3 hours of One-on-One online coaching on web conferencing tools and how to use them for your business. Includes access to online resource library of our Online Facilitator Certification plus access to your own online meeting room and virtual collaboration platform ($1,900).</p></li>
    <li class="service s3"><p><svg class="service-arrow" viewBox="0 0 12 10"><path d="M0 3.5H7V0L12 5L7 10V6.5H0Z" fill="var(--arrow)"/></svg>Outfitting the Online Entrepreneur: 4-hours of One-on-One online coaching to learn about web conferencing tools and how to use them for your business. Includes access to online resource library of our Online Facilitator Certification plus access to your own online meeting room and virtual collaboration platform ($1,300).</p></li>
    <li class="service s4"><p><svg class="service-arrow" viewBox="0 0 12 10"><path d="M0 3.5H7V0L12 5L7 10V6.5H0Z" fill="var(--arrow)"/></svg>Outfitting the Online Educator: 3-hours of One-on-One online coaching to learn about web conferencing tools and how to use them for your training sessions. Includes access to online resource library of our Online Facilitator Certification plus access to your own online meeting room and virtual collaboration platform ($1,200).</p></li>
    <li class="service s5"><p><svg class="service-arrow" viewBox="0 0 12 10"><path d="M0 3.5H7V0L12 5L7 10V6.5H0Z" fill="var(--arrow)"/></svg>Repurposing for Online Audiences: Design and develop materials, agenda, event plans and activities to repurpose your face-to-face session for online sessions that market your expertise. Includes 2-hours of One-on-One online coaching to learn about web conferencing tools and how to use them for your business ($500).</p></li>
    <li class="service s6"><p><svg class="service-arrow" viewBox="0 0 12 10"><path d="M0 3.5H7V0L12 5L7 10V6.5H0Z" fill="var(--arrow)"/></svg>One-on-one coaching with resources: 2-hours of One-on-One online coaching to learn about web conferencing tools and how to use them for your business. Includes access to online resource library of our Online Facilitator Certification ($300).</p></li>
    <li class="service s7"><p><svg class="service-arrow" viewBox="0 0 12 10"><path d="M0 3.5H7V0L12 5L7 10V6.5H0Z" fill="var(--arrow)"/></svg>One-on-one coaching: 2-hours of One-on-One online coaching to learn about web conferencing tools and how to use them for your business. Includes three job aids for online facilitators ($200)</p></li>
  </ul>

  <div class="intro">
    <p>You'll participate via the Convenia Roomkit platform. No special software is required. If you have a computer with Internet access and a direct telephone line you have all is needed to participate.</p>
    <p>As a professional communicators – whether you are a small business owner, an educator or a manager - you know that webinar technology is here to stay. Have you wondered how to use them to benefit your business or your organization? Leave the details to us. Well implemented online sessions can give your business unparalleled access to new markets and potential new clients at a minimum cost.</p>
  </div>

  <div class="call">Want to know more? <strong>Call us at</strong> <span class="phone">555-0148-2290</span></div>
</div>
</body>
</html>
```